Motorcycle Mechanic - Van and Business Card Design

Need a van and business card designed for a company called Gear Mend.

Gearmend is a mobile motorcycle mechanic based in Sydney Australia. The goal of the design is to stand out look modern. The van is Black and generally the designs will be on a darker colour using brighter colours to contrast and grab attention.

Company Colours are slightly off black (background) and yellow, slightly off white.

Really like the designs of energy drink vehicles (https://plorvexmedia.example-files.net/2012/11/van-wraps-pkg-sample.jpg?w=1500) and velkranbitter (http://blog.quillardstudio.com.au/wp-content/uploads/2008/03/utevectorside.jpg) promotional vehicles.

Details on car to include:

Website: gear-mend.com.au
Phone: 9134 2718
Services: Servicing, Repairs, Pickup & Emergency Callouts

*The above on both side panels & rear of van
*If services too hard to fit everything on rear prioritise the logo, phone number and website.

Car is a 2014 Black, Dorven Trask.- See images attached for reference.

Files to be provided in .ai or .eps.

Business card details:

Dimensions: 85mm x 54mm
Bleed: 2mm

Name: Tomas Rudlow
Phone: 9134 2718
Email: tomas@gear-mend.com.au

Logo to be included on either both or one side. Base of card should be dark close to black for at least one side (ok for both, designers call).

Target Market(s)

Bike Owners

Industry/Entity Type

Mechanic

Font styles to use
Sans Serif

Requirements
Must have
• Files in .ai or .eps
• Must catch attention without looking tacky.
• Must have details mentioned in the product description.
Nice to have
• Graphical elements that bring attention to important information.
Should not have
• Any non vector imagery. Any clipart of photographic type imagery. Too many colours. Any imagery or graphics that breach trademarks or copyright laws.

```html
<!DOCTYPE html>
<html lang="en">
<head>
<meta charset="utf-8">
<title>Gear Mend – Business Card</title>
<link rel="stylesheet" href="https://fonts.googleapis.com/css2?family=Montserrat:wght@400;500;700&display=swap">
<style>
  :root {
    --stage: #e6e4e0;
    --card-black: #0b0b0b;
    --brand-yellow: #f7c600;
    --off-white: #f4f2ee;
    --ink: #111111;
  }
  * { box-sizing: border-box; margin: 0; padding: 0; }
  html, body {
    width: 1200px; height: 800px; overflow: hidden;
    background: var(--stage);
    font-family: "Montserrat", sans-serif;
  }
  .stage {
    position: relative; width: 1200px; height: 800px;
    display: flex; align-items: center; justify-content: center; gap: 60px;
  }
  .card {
    position: relative; width: 520px; height: 330px;
    background: var(--card-black); overflow: hidden;
    box-shadow: 0 10px 28px rgba(0,0,0,0.18);
  }
  .brand {
    display: flex; align-items: center; gap: 12px;
    color: var(--off-white); font-weight: 700; letter-spacing: 0.04em;
  }
  .brand-square { background: var(--brand-yellow); flex: none; }

  /* Front */
  .card-front .top-tab {
    position: absolute; top: 0; left: 248px; width: 118px; height: 16px;
    background: var(--brand-yellow); border-radius: 0 0 6px 6px;
  }
  .card-front .brand {
    position: absolute; left: 50%; top: 50%; transform: translate(-50%, -50%);
    font-size: 38px;
  }
  .card-front .brand-square { width: 34px; height: 34px; }

  /* Back */
  .card-back .logo-side {
    position: absolute; left: 0; top: 0; width: 238px; height: 100%;
    background: var(--card-black);
  }
  .card-back .side-tab {
    position: absolute; left: 0; top: 36px; width: 16px; height: 80px;
    background: var(--brand-yellow); border-radius: 0 6px 6px 0;
  }
  .card-back .brand {
    position: absolute; left: 50%; top: 50%; transform: translate(-50%, -50%);
    font-size: 20px; gap: 8px;
  }
  .card-back .brand-square { width: 18px; height: 18px; }
  .card-back .contact-side {
    position: absolute; left: 238px; top: 0; right: 0; height: 100%;
    background: var(--brand-yellow); color: var(--ink);
    padding: 118px 0 0 36px;
  }
  .card-back .right-tab {
    position: absolute; right: 0; top: 196px; width: 16px; height: 84px;
    background: var(--card-black); border-radius: 6px 0 0 6px;
  }
  .holder-name { font-size: 21px; font-weight: 700; margin-bottom: 14px; }
  .contact-line {
    display: flex; align-items: center; gap: 12px;
    font-size: 14px; font-weight: 500; margin-bottom: 9px;
  }
  .contact-line svg { width: 16px; height: 16px; flex: none; }
</style>
</head>
<body>
<main class="stage">
  <section class="card card-front" aria-label="Business card front">
    <div class="top-tab"></div>
    <div class="brand"><span class="brand-square"></span><span>GEARMEND</span></div>
  </section>

  <section class="card card-back" aria-label="Business card back">
    <div class="logo-side">
      <div class="side-tab"></div>
      <div class="brand"><span class="brand-square"></span><span>GEARMEND</span></div>
    </div>
    <div class="contact-side">
      <p class="holder-name">Tomas Rudlow</p>
      <p class="contact-line">
        <svg viewBox="0 0 16 16" aria-hidden="true"><rect x="4" y="1" width="8" height="14" rx="1.5" fill="none" stroke="currentColor" stroke-width="1.4"/><line x1="7" y1="12.5" x2="9" y2="12.5" stroke="currentColor" stroke-width="1.2"/></svg>
        <span>9134 2718</span>
      </p>
      <p class="contact-line">
        <svg viewBox="0 0 16 16" aria-hidden="true"><rect x="1.5" y="3.5" width="13" height="9" fill="none" stroke="currentColor" stroke-width="1.4"/><polyline points="1.5,3.5 8,9 14.5,3.5" fill="none" stroke="currentColor" stroke-width="1.4"/></svg>
        <span>tomas@gear-mend.com.au</span>
      </p>
    </div>
    <div class="right-tab"></div>
  </section>
</main>
</body>
</html>
```